Homepage design for female-owned English/French speaking Law firm

Brief Update - we prefer not to have a photo of a person in the hero shot

Morlewy.com.au is the website for a English/French Bilingual Female-owned Law Firm, Quillomette Morlewy.
Overall Design notes:
Professional, yet warm and welcoming
Historic foundations but Progressive, woman-owned, sleek, innovative and modern.
Approachable, casual yet professional. Sans-serif font and light colours would help this
2 languages switched by flags (English/French)

Winner must provide
Home page design
Standard (inner) page design (can be provided after winner is selected)
All photos used in the design without charge

Number of Pages Required

2 page

Requirements
Should not have
• Update - we prefer not to have a photo of a person in the hero shot

```html
<!DOCTYPE html>
<html lang="en">
<head>
<meta charset="utf-8">
<title>Quillomette Morlewy</title>
<link href="https://fonts.googleapis.com/css2?family=Inter:wght@400;500;600;700&display=swap" rel="stylesheet">
<style>
:root{
  --orange:#fb8c2b;
  --ink:#2b2b2b;
  --text:#3a3a3a;
  --muted:#6b6b6b;
  --sand:#dfd2c6;
  --line:#d8d8d8;
}
*{box-sizing:border-box;margin:0;padding:0}
html,body{width:1200px;height:2928px;overflow:hidden}
body{font-family:"Inter",sans-serif;color:var(--text);background:#fff;position:relative}
.abs{position:absolute}
.orange{color:var(--orange)}
.btn{position:absolute;display:flex;align-items:center;justify-content:center;font-weight:600;font-size:14px;height:42px;width:200px}
.btn-fill{background:var(--orange);color:#fff}
.btn-line{border:2px solid var(--orange);color:var(--orange)}

.topbar{left:67px;right:67px;top:0;height:37px;border-bottom:1px solid var(--line);display:flex;align-items:center;gap:22px;font-size:11px;color:var(--ink)}
.topbar span{display:flex;align-items:center;gap:8px}
.flag{position:absolute;right:0;top:10px;display:flex;align-items:center;gap:8px}

.hero{left:0;top:0;width:1200px;height:720px;background:linear-gradient(180deg,#fff 0%,#f8eee6 45%,#efdccc 100%)}
.wordmark{position:absolute;display:flex;align-items:center;gap:10px;font-weight:600;color:var(--ink);white-space:nowrap}
.wordmark i{display:block;background:var(--orange)}
.nav{position:absolute;top:68px;left:600px;display:flex;gap:28px;font-size:14px;font-weight:500;color:var(--ink)}
.hero h1{position:absolute;top:180px;left:0;width:1200px;text-align:center;font-size:78px;line-height:90px;font-weight:600;color:var(--ink);letter-spacing:-1px}
.hero p{position:absolute;top:482px;left:240px;width:720px;text-align:center;font-size:13px;line-height:16px;color:var(--muted)}

.stats{left:67px;top:655px;width:1066px;height:157px;background:#fff;display:flex}
.stat{flex:1;text-align:center;padding-top:40px;position:relative}
.stat+.stat:before{content:"";position:absolute;left:0;top:55px;height:48px;border-left:2px solid #ccc}
.stat div:first-child{font-size:14px;color:var(--ink)}
.stat div:last-child{font-size:46px;font-weight:600;color:var(--orange);margin-top:10px}

.section-title{position:absolute;left:0;width:1200px;text-align:center;font-size:44px;font-weight:500;color:var(--ink)}
.dash{position:absolute;left:588px;width:24px;height:6px;background:#8a8a8a}
.about{left:0;top:812px;width:1200px;height:446px;background:linear-gradient(180deg,#f3ebe4 0%,#eadccf 55%,#d9c7b8 100%)}
.about ul{position:absolute;left:250px;width:700px;top:160px;list-style:none;text-align:center;font-size:14px;line-height:21px;color:var(--ink)}
.about li{margin-bottom:21px}
.about li:before{content:"• "}

.services-sub{position:absolute;top:1385px;left:0;width:1200px;text-align:center;font-size:14px;color:var(--muted)}
.card{position:absolute;width:253px;height:198px;display:flex;flex-direction:column;align-items:center;justify-content:center;text-align:center;font-size:14px;font-weight:600;color:#555;line-height:16px}
.card svg{margin-bottom:18px}
.card.active{border:2px solid var(--orange);color:var(--orange)}

.contact-photo{left:0;top:1926px;width:600px;height:539px;background:linear-gradient(180deg,#f6f0eb 0%,#e6d9cd 50%,#cdbcad 100%)}
.contact-form{left:600px;top:1926px;width:600px;height:539px;background:var(--sand)}
.label{position:absolute;left:42px;font-size:13px;font-weight:600;color:var(--ink)}
.label b{color:#e33}
.field{position:absolute;left:42px;width:451px;height:42px;background:#fff;border:1px solid #bbb;border-radius:6px;padding:12px 16px;font-size:13px;color:#888}
.info{position:absolute;font-size:14px;line-height:27px;color:var(--ink)}
.info span{display:flex;align-items:center;gap:10px}

.footer{left:0;top:2465px;width:1200px;height:463px;background:#fff}
.fcol{position:absolute;top:2538px;font-size:13px;font-weight:500;color:var(--ink)}
.fcol h4{font-size:17px;font-weight:500;color:var(--orange);margin-bottom:20px}
.fcol p{margin-bottom:19px}
</style>
</head>
<body>

<section class="abs hero">
  <div class="topbar abs">
    <span><svg width="12" height="9" viewBox="0 0 12 9"><rect width="12" height="9" fill="#333"/><path d="M0 0l6 5 6-5" stroke="#fff" fill="none"/></svg>claire@morlewy.com.au</span>
    <span><svg width="11" height="11" viewBox="0 0 24 24"><path fill="#333" d="M6.6 10.8a15 15 0 006.6 6.6l2.2-2.2c.3-.3.7-.4 1-.2 1.1.4 2.3.6 3.6.6.6 0 1 .4 1 1V20c0 .6-.4 1-1 1A17 17 0 013 4c0-.6.4-1 1-1h3.5c.6 0 1 .4 1 1 0 1.3.2 2.5.6 3.6.1.3 0 .7-.2 1z"/></svg>(+612) 9000 4188</span>
    <span><svg width="11" height="11" viewBox="0 0 12 12"><circle cx="6" cy="6" r="4" fill="none" stroke="#333" stroke-width="2"/></svg>Migration Agent’s registration No : 1000527</span>
    <div class="flag"><svg width="28" height="18" viewBox="0 0 3 2"><rect width="1" height="2" fill="#1f3fa8"/><rect x="1" width="1" height="2" fill="#fff"/><rect x="2" width="1" height="2" fill="#e0262f"/></svg><svg width="10" height="6" viewBox="0 0 10 6"><path d="M1 1l4 4 4-4" stroke="#333" fill="none" stroke-width="1.5"/></svg></div>
  </div>
  <div class="wordmark" style="left:67px;top:64px;font-size:20px"><i style="width:14px;height:14px"></i>Quillomette Morlewy</div>
  <nav class="nav"><span>Home</span><span>About us</span><span>Our service ⌄</span><span>Download &amp; Link</span></nav>
  <div class="btn btn-fill" style="left:997px;top:56px;width:137px">Contact us</div>
  <h1>WE ARE A <span class="orange">FIRM OF<br>FRENCH-SPEAKING</span><br>LAWYERS</h1>
  <p>located in the Sydney central business district. We provide a broad range of legal services in English and French to clients in Australia and overseas.</p>
  <div class="btn btn-fill" style="left:387px;top:550px">Appointment now</div>
  <div class="btn btn-line" style="left:613px;top:550px">Lean more</div>
</section>

<div class="abs stats">
  <div class="stat"><div>Founded in</div><div>1930s</div></div>
  <div class="stat"><div>Trusted customer</div><div>5000+</div></div>
  <div class="stat"><div>Successful Case</div><div>4560+</div></div>
  <div class="stat"><div>Case Closed</div><div>3500+</div></div>
</div>

<section class="abs about" role="img" aria-label="Soft sunset photograph of the Sydney Opera House by the harbour">
  <div class="section-title" style="top:65px">ABOUT <span class="orange">US</span></div>
  <div class="dash" style="top:124px"></div>
  <ul>
    <li>Our small, skilled team is committed to the delivery of quality legal services to our clients.</li>
    <li>Quillomette Morlewy originated with the legal practice founded by Mr Lucien Armand Quillomette in the 1930s. Today, we are a progressive law firm that has embraced both the traditional approach of our predecessor firms and the efficiencies of modern technology.</li>
    <li>All of our services are available in English or in French according to the needs of our clients.</li>
  </ul>
  <div class="btn btn-fill" style="left:500px;top:338px">Learn more</div>
</section>

<div class="section-title" style="top:1318px">OUR <span class="orange">SERVICES</span></div>
<p class="services-sub">If you have a question relating to other areas of law, please do not hesitate to contact us for referral to an expert in the relevant field.</p>
<div class="dash" style="top:1414px"></div>

<div class="card active" style="left:67px;top:1462px"><svg width="56" height="56" viewBox="0 0 56 56" fill="none" stroke="#fb8c2b" stroke-width="2"><path d="M4 24L28 6l24 18M10 22v28h36V22M18 50V34h20v16M22 34v16M28 34v16M34 34v16M14 12h16"/></svg>Property Law including<br>Conveyancing &amp; Leases.</div>
<div class="card" style="left:338px;top:1462px"><svg width="56" height="56" viewBox="0 0 56 56" fill="none" stroke="#666" stroke-width="2"><rect x="4" y="16" width="48" height="32"/><path d="M20 16V9h16v7M4 30h48M24 27v6h8v-6"/></svg>Sale &amp; Purchase of<br>Business.</div>
<div class="card" style="left:609px;top:1462px"><svg width="56" height="56" viewBox="0 0 56 56" fill="none" stroke="#666" stroke-width="2"><path d="M12 4h22l10 10v38H12zM34 4v10h10M18 26h20M18 32h20M18 38h20M18 44h14"/></svg>Deceased Estates &amp;<br>Wills.</div>
<div class="card" style="left:880px;top:1462px"><svg width="56" height="56" viewBox="0 0 56 56"><path d="M4 12l24 4v36L4 48z" fill="#fff" stroke="#555" stroke-width="2"/><path d="M28 16l24-8v36l-24 8z" fill="#444"/><text x="9" y="38" font-size="16" fill="#444">文</text><text x="34" y="38" font-size="18" font-weight="700" fill="#fff">A</text></svg>Translation service.</div>

<div class="card" style="left:67px;top:1672px"><svg width="56" height="56" viewBox="0 0 56 56" fill="none" stroke="#666" stroke-width="2"><path d="M4 8h48v30H30l-10 10v-10H4zM12 16h32M12 22h32M12 28h24"/></svg>Advice in relation to<br>transactions in France.</div>
<div class="card" style="left:338px;top:1672px"><svg width="56" height="56" viewBox="0 0 56 56" fill="none" stroke="#666" stroke-width="2"><path d="M6 6v44h46M10 38l8-14 8 8 8-16 8 10 8-6"/></svg>Affairs Management.</div>
<div class="card" style="left:609px;top:1672px"><svg width="56" height="56" viewBox="0 0 56 56" fill="#555"><circle cx="26" cy="9" r="5"/><path d="M20 17h12v18h-3v17h-6V35h-3z"/><path d="M34 26v26" stroke="#555" stroke-width="2"/></svg>Elder Law.</div>
<div class="card" style="left:880px;top:1672px"><svg width="56" height="56" viewBox="0 0 56 56" fill="#555"><circle cx="20" cy="9" r="5"/><path d="M14 17h12v16h-3v17h-6V33h-3z"/><path d="M30 24h20M40 20v20M34 34h12" stroke="#555" stroke-width="2" fill="none"/></svg>Powers of Attorney /<br>Guardianship.</div>

<section class="abs contact-photo" role="img" aria-label="Faded photograph of the Sydney Opera House steps">
  <div class="section-title" style="top:45px;width:600px">GET IN <span class="orange">TOUCH</span></div>
  <p class="abs" style="top:116px;left:0;width:600px;text-align:center;font-size:14px;line-height:21px;color:var(--muted)">Looking for good lawyer? , Don’t be shy.<br>Let’s work together.</p>
  <div class="dash" style="top:162px;left:288px"></div>
  <div class="info" style="left:67px;top:213px">Level 9, 48 Harrow street<br>Sydney, NSW 2000<br>Australia</div>
  <div class="info" style="left:350px;top:207px">
    <span><svg width="11" height="11" viewBox="0 0 24 24"><path fill="#333" d="M6.6 10.8a15 15 0 006.6 6.6l2.2-2.2c.3-.3.7-.4 1-.2 1.1.4 2.3.6 3.6.6.6 0 1 .4 1 1V20c0 .6-.4 1-1 1A17 17 0 013 4c0-.6.4-1 1-1h3.5c.6 0 1 .4 1 1 0 1.3.2 2.5.6 3.6.1.3 0 .7-.2 1z"/></svg>Phone: (+612) 9000 4188</span>
    <span><svg width="11" height="11" viewBox="0 0 12 12"><rect x="1" y="3" width="10" height="7" fill="#333"/><rect x="3" y="0" width="6" height="3" fill="#333"/></svg>Fax: (+612) 9000 4133</span>
    <span><svg width="11" height="9" viewBox="0 0 12 9"><rect width="12" height="9" fill="#333"/><path d="M0 0l6 5 6-5" stroke="#fff" fill="none"/></svg>E-mail: claire@morlewy.com.au</span>
  </div>
</section>

<section class="abs contact-form">
  <div class="label" style="top:22px">Full name <b>*</b></div>
  <div class="field" style="top:50px">Full name</div>
  <div class="label" style="top:104px">Email <b>*</b></div>
  <div class="field" style="top:132px">Youremail@address.com</div>
  <div class="label" style="top:186px">Phone number</div>
  <div class="field" style="top:214px;width:310px">Phone number</div>
  <div class="label" style="top:268px">Message <b>*</b></div>
  <div class="field" style="top:296px;height:154px">How we can help you?</div>
  <div class="btn btn-fill" style="left:42px;top:476px">Send</div>
</section>

<footer class="abs footer">
  <div class="wordmark" style="left:67px;top:66px;font-size:26px"><i style="width:18px;height:18px"></i>Quillomette Morlewy</div>
  <p class="abs" style="left:67px;top:157px;width:330px;font-size:13px;line-height:21px;color:var(--text)">Lorem ipsum dolor sit amet consectetur. Elit vitae fringilla quisque dictum cras urna lacus tristique et.</p>
  <p class="abs" style="left:67px;top:418px;font-size:11px;color:var(--muted)">2024 © Copyright, quillomette morlewy. All rights reserved.</p>
</footer>
<div class="fcol" style="left:518px"><h4>Get to know us</h4><p>Home</p><p>About us</p><p>Download &amp; Link</p></div>
<div class="fcol" style="left:698px"><h4>Our service</h4><p>Property law</p><p>Sale of Business</p><p>Wills &amp; Estates</p><p>Translation</p><p>Elder Law</p><p>Powers of Attorney</p><p>French advice</p><p>Affairs management</p></div>
<div class="fcol" style="left:879px"><h4>Contact us</h4><p style="line-height:16px">Level 9, 48 Harrow street<br>Sydney, NSW 2000<br>Australia</p><p>Phone: (+612) 9000 4188</p><p>Fax: (+612) 9000 4133</p><p>E-mail: claire@morlewy.com.au</p></div>

</body>
</html>
```